Crumb Joy pastry business card design

I need a logo and a business card design for my baking business, "Crumb Joy". I daily bake French pastries from scratch using high quality ingredients and directly cater to local customers. My product is very authentic but sold at a casual setting . I'm looking for a simple, cute, stylish yet earthy design. Like this kind of feel:
http://clipvista.example/71946302
Target Market(s)
Metropolitan food conscious consumers in their 20-40s
Industry/Entity Type
Business
Requirements
Must have
- Soft pastel colors or other types of color schemes that would remind French pastries.
email: welovecrumbles@mailnest.example
twitter@bitemesf
www.crumbjoyla.example
Nice to have
Should not have
- pictures of pastries - sketches are ok.

```html
<!DOCTYPE html>
<html lang="en">
<head>
<meta charset="utf-8">
<title>Crumb Joy Pastry – Business Card Concepts</title>
<link rel="stylesheet" href="https://fonts.googleapis.com/css2?family=Jost:wght@300;400;500&display=swap">
<style>
  :root {
    --page: #ffffff;
    --apricot: #f8d294;
    --ink: #1e1a17;
    --ink-soft: #5a5653;
    --card-text: #ffffff;
    --photo-light: #f3ece4;
    --photo-mid: #e2d4c2;
    --photo-warm: #d8c1a1;
    --label: #111111;
  }
  * { box-sizing: border-box; margin: 0; padding: 0; }
  html, body { width: 881px; height: 1200px; overflow: hidden; background: var(--page); }
  body { position: relative; font-family: "Jost", "Futura", sans-serif; }

  .card {
    position: absolute;
    width: 211px;
    height: 367px;
    overflow: hidden;
  }
  .card--short { height: 356px; }
  .card--back { background: var(--apricot); color: var(--card-text); text-align: center; }

  .card__photo {
    position: absolute; inset: 0;
    background:
      radial-gradient(ellipse 70% 40% at 55% 45%, var(--photo-light) 0%, transparent 70%),
      linear-gradient(180deg, var(--photo-light) 0%, var(--photo-mid) 45%, var(--photo-warm) 65%, var(--photo-mid) 80%, var(--photo-light) 100%);
  }

  .wordmark {
    position: absolute; left: 0; right: 0;
    text-align: center;
    font-weight: 400;
    line-height: 1.05;
    letter-spacing: 0.04em;
  }
  .wordmark--front { top: 128px; font-size: 27px; color: var(--ink); }
  .wordmark--front-tall { top: 118px; font-size: 31px; font-weight: 300; color: var(--ink); letter-spacing: 0.08em; }
  .wordmark--bold { top: 138px; font-weight: 500; }
  .wordmark--lighter { color: var(--ink-soft); }
  .wordmark--back { top: 60px; font-size: 22px; color: var(--card-text); }
  .wordmark--back-tall { top: 52px; font-size: 25px; font-weight: 300; color: var(--card-text); letter-spacing: 0.08em; }
  .wordmark--back-bold { top: 88px; font-weight: 500; }

  .contact {
    position: absolute; left: 0; right: 0;
    list-style: none;
    font-size: 12.5px;
    line-height: 1.22;
  }
  .contact li { margin-bottom: 10px; }
  .contact--row1 { top: 146px; }
  .contact--row2 { top: 143px; }
  .contact--row3 { top: 150px; }

  .bite { position: absolute; top: 0; width: 80px; height: 50px; }
  .bite--left { left: 0; }
  .bite--right { right: 0; }

  .caption { position: absolute; font-size: 13px; font-weight: 500; color: var(--label); }
  .caption--front { left: 228px; top: 393px; }
  .caption--back { left: 477px; top: 393px; }
  .caption--lighter { left: 826px; top: 1155px; line-height: 1.15; }
</style>
</head>
<body>

  <!-- Concept one -->
  <section class="card card--front" style="left:142px; top:0;">
    <div class="card__photo" role="img" aria-label="Soft, faded photograph of a sugar-dusted cream pastry on a plate"></div>
    <p class="wordmark wordmark--front">Crumb Joy<br>PASTRY</p>
  </section>
  <section class="card card--back" style="left:390px; top:0; height:371px;">
    <p class="wordmark wordmark--back">Crumb Joy<br>PASTRY</p>
    <ul class="contact contact--row1">
      <li>Name</li>
      <li>3185 402 617</li>
      <li>214 Oven Lane<br>Crumbton NT</li>
      <li>welovecrumbles@mailnest.example</li>
      <li>twitter@crumbjoyla</li>
      <li>www.crumbjoyla.example</li>
    </ul>
  </section>
  <p class="caption caption--front">Front</p>
  <p class="caption caption--back">Back</p>

  <!-- Concept two -->
  <section class="card card--front" style="left:142px; top:433px;">
    <div class="card__photo" role="img" aria-label="Soft, faded photograph of a sugar-dusted cream pastry on a plate"></div>
    <p class="wordmark wordmark--front-tall">CRUMB JOY<br>PASTRY</p>
  </section>
  <section class="card card--back" style="left:390px; top:433px; height:370px;">
    <p class="wordmark wordmark--back-tall">CRUMB JOY<br>PASTRY</p>
    <ul class="contact contact--row2">
      <li>Name</li>
      <li>3185 402 617</li>
      <li>214 Oven Lane<br>Crumbton NT</li>
      <li>welovecrumbles@mailnest.example</li>
      <li>twitter@crumbjoyla</li>
      <li>www.crumbjoyla.example</li>
    </ul>
  </section>

  <!-- Concept three: bitten corner -->
  <section class="card card--front card--short" style="left:84px; top:840px;">
    <div class="card__photo" role="img" aria-label="Soft, faded photograph of a sugar-dusted cream pastry on a plate"></div>
    <p class="wordmark wordmark--front wordmark--bold">Crumb Joy<br>PASTRY</p>
    <svg class="bite bite--left" viewBox="0 0 80 50" aria-hidden="true">
      <g fill="#ffffff">
        <circle cx="0" cy="30" r="16"/><circle cx="14" cy="13" r="14"/>
        <circle cx="34" cy="2" r="14"/><circle cx="56" cy="-4" r="12"/>
      </g>
    </svg>
  </section>
  <section class="card card--back card--short" style="left:336px; top:840px;">
    <p class="wordmark wordmark--back wordmark--back-bold">Crumb Joy<br>PASTRY</p>
    <ul class="contact contact--row3">
      <li>3185 402 617</li>
      <li>214 Oven Lane<br>Crumbton NT</li>
      <li>welovecrumbles@mailnest.example</li>
      <li>twitter@crumbjoyla</li>
      <li>www.crumbjoyla.example</li>
    </ul>
    <svg class="bite bite--right" viewBox="0 0 80 50" aria-hidden="true">
      <g fill="#ffffff">
        <circle cx="80" cy="30" r="16"/><circle cx="66" cy="13" r="14"/>
        <circle cx="46" cy="2" r="14"/><circle cx="24" cy="-4" r="12"/>
      </g>
    </svg>
  </section>
  <section class="card card--front card--short" style="left:600px; top:834px;">
    <div class="card__photo" role="img" aria-label="Soft, faded photograph of a sugar-dusted cream pastry on a plate"></div>
    <p class="wordmark wordmark--front wordmark--bold wordmark--lighter">Crumb Joy<br>PASTRY</p>
    <svg class="bite bite--left" viewBox="0 0 80 50" aria-hidden="true">
      <g fill="#ffffff">
        <circle cx="0" cy="30" r="16"/><circle cx="14" cy="13" r="14"/>
        <circle cx="34" cy="2" r="14"/><circle cx="56" cy="-4" r="12"/>
      </g>
    </svg>
  </section>
  <p class="caption caption--lighter">Lighter<br>Text</p>

</body>
</html>
```